Dynamic Lead Design (Partial WebPage)

To encourage visitors to our website to donate to our organization, we would like to replace the Dynamic Lead on our website with one that will evoke emotion from the viewer and motivate them to donate generously.

The deliverable should be a mockup of the design in context of the current website. See attached file for editable area. Fonts used in the mockup should be code-able in HTML/CSS.

The website
http://www.hopelark.org

Please use this wireframe for reference:
http://app.mockvane.com/8b1c47e20f93d5a6c71e04b28d9a3f5e17c6b0d2/7315824

Content:
[Image should evoke emotion from the viewer and motivate them to donate generously.]
Headline - “Give to TIDEL.”
Sub Headline - “Cancer patients find answers here. Your donation makes that possible.”
Call to action label - “Donate”

We love these examples:

Bright Oak Harvest Drive (http://www.hd.brightoak.org/brightoak/v/index.jsp?vgnextoid=7a5d3f81c2e9b460VgnVCM100000318274bdRCRD)
Well Meadow (http://www.wellmeadow.org/)

Design Size:
width: 971px
height: 300px

***see attached document for design area***

- Organization Background -

Our website receives over 40,000 unique visitors each month - mostly cancer patients and their family members seeking information about their disease. We would like to drive our visitors to donate to our nonprofit throughout late November and December (the majority of our donations from individuals come in during that time period).

We will be mailing an appeal letter to our database in mid-November. With this banner ad, we seek to complement that appeal. Some key messages from our appeal are:

- We focus on getting patients and their loved ones the best, most up-to-date information from trusted doctors who are leaders in cancer research – for free. We don’t sell a particular product or procedure. We simply arm them with the most current information so they can make the best decision for their own (or their loved one’s) care.

- What is the value of the support they or someone they know has received from our organization? Twenty-five dollars? One hundred dollars? One thousand? Can you even put an amount to it? Whatever it is, please consider making an end of year donation to this organization that has helped so many, comforted hundreds of thousands of patients and caretakers, and been there when needed.

- 2014 will be a year of growth. We just hired our first executive director. She is experienced in helping small nonprofits grow in size, revenue, and scope, and will undoubtedly bring a new level of energy to our work.

- In just a few months, we will hold two patient forums – first-of-its-kind programs for the organization. As we continue to grow, we will be able to offer more of these types of programs to more patients throughout the US.

Industry/Entity Type

Charity

Requirements
Must have
• - Must Adhere to existing website branding

```html
<!DOCTYPE html>
<html lang="en">
<head>
<meta charset="utf-8">
<title>TIDEL – Give to TIDEL</title>
<link rel="stylesheet" href="https://fonts.googleapis.com/css2?family=Arimo:wght@400;700&family=Barlow:wght@500;600;700&display=swap">
<style>
:root{
  --mint:#8ccaa4;
  --salmon:#e49a83;
  --slate:#7b7b7b;
  --taupe:#a09288;
  --green-link:#4d8a4f;
  --text:#333;
  --orange:#eb9a2a;
  --brick:#8f2a14;
  --rule:#dcdcdc;
}
*{box-sizing:border-box;margin:0;padding:0}
html,body{width:1046px;height:1200px;overflow:hidden;background:#fff}
body{position:relative;font-family:"Arimo",Arial,sans-serif;color:var(--text)}
a{text-decoration:none;color:inherit}

.brand{position:absolute;left:44px;top:36px;display:flex;align-items:center;gap:14px}
.brand-dot{width:80px;height:80px;border-radius:50%;background:var(--salmon)}
.brand-name{font-family:"Barlow",sans-serif;font-weight:700;font-size:40px;color:var(--slate);letter-spacing:1px}

.search{position:absolute;left:474px;top:44px;width:404px;height:58px;border:3px solid #cfe8d8;border-radius:22px;background:#fff;display:flex;align-items:center;padding:0 10px 0 26px;gap:6px}
.search-field{width:286px;height:24px;border:1px solid #ccc;font-size:10px;color:#888;padding:5px 4px}
.search-btn{background:#cde6d6;border:1px solid #a8cdb5;border-radius:3px;font-size:11px;font-weight:700;padding:5px 8px}
.search-clear{color:#777;font-size:13px;margin-left:4px}

.nav{position:absolute;left:44px;top:151px;width:970px;height:45px;display:flex;gap:3px}
.nav-tab{background:var(--mint);color:#fff;font-family:"Barlow",sans-serif;font-weight:600;font-size:15px;letter-spacing:1.2px;text-transform:uppercase;line-height:15px;display:flex;align-items:center;justify-content:center;text-align:center}
.nav-tab.about{width:167px}
.nav-tab.ask{width:171px;font-size:14px}
.nav-tab.general,.nav-tab.focused{width:170px}
.nav-tab.profile{width:139px;background:var(--slate)}
.nav-tab.donate{width:139px;background:var(--salmon);position:relative}
.donate-badge{position:absolute;right:0;top:-37px;width:56px;height:42px;background:var(--salmon);border-radius:28px 28px 0 0;display:flex;align-items:center;justify-content:center}

.lead{position:absolute;left:44px;top:196px;width:970px;height:300px;background:linear-gradient(90deg,#c9c3b7 0%,#efc9b7 25%,#e7c1c4 42%,#a9a889 65%,#8f9a74 100%);overflow:hidden}
.lead-title{position:absolute;right:40px;top:40px;font-family:"Barlow",sans-serif;font-weight:700;font-size:62px;line-height:66px;color:var(--orange);white-space:nowrap}
.lead-sub{position:absolute;left:535px;top:108px;width:400px;text-align:center;color:#fff;font-family:"Barlow",sans-serif;font-weight:600;font-size:20px;line-height:36px}
.lead-cta{position:absolute;left:633px;top:198px;width:206px;height:42px;border-radius:20px;background:linear-gradient(#b8401f,var(--brick));color:#fff;font-family:"Barlow",sans-serif;font-weight:600;font-size:22px;display:flex;align-items:center;justify-content:center;box-shadow:0 2px 3px rgba(0,0,0,.35)}
.lead-underline{position:absolute;left:44px;top:496px;width:970px;height:2px;background:#e2e2e2}

.edit{position:absolute;left:55px;top:515px;font-size:13px;font-weight:700;color:#444}

.news{position:absolute;left:44px;top:565px;width:688px}
.news-head{display:flex;justify-content:space-between;align-items:flex-start}
.news-title{font-size:17px;font-weight:700;color:#666;margin-top:11px}
.share{display:flex;align-items:center;gap:2px;border:1px solid #ccc;padding:1px 3px;font-size:12px;margin-right:16px}
.share i{width:12px;height:12px;display:inline-block;background:#7d9bc4}
.share i:nth-child(2){background:#8ccbe8}.share i:nth-child(3){background:#333}.share i:nth-child(4){background:#4a7bd2;margin-right:4px}
.post{border-bottom:1px solid var(--rule);padding:28px 0 27px}
.post:first-of-type{padding-top:46px}
.post:last-child{border:0}
.post-title{font-size:17px;font-weight:700;color:var(--green-link);line-height:21px}
.post-meta{font-size:14px;color:#444;margin-top:3px;word-spacing:3px}
.post-meta b{color:#444}
.post-meta .cat{color:var(--green-link);font-weight:700;word-spacing:0}
.post-text{font-size:16px;line-height:20px;margin-top:20px}
.post-text em{color:var(--green-link);font-size:14px}

.side{position:absolute;left:757px;top:518px;width:243px}
.social{display:flex;gap:22px;margin-left:26px}
.social span{width:32px;height:32px;border-radius:5px}
.ask-box{margin-top:22px;height:45px;background:var(--salmon);display:flex;align-items:center;padding-left:8px;gap:6px;color:#fff;font-family:"Barlow",sans-serif;font-size:20px;letter-spacing:1px}
.ask-box .qa{width:33px;height:33px;border-radius:50%;background:#888;display:flex;align-items:center;justify-content:center;font-size:17px}
.ask-box .label{margin-left:14px}
.side h3{font-size:17px;color:#666;margin-top:26px}
.side-links a{display:block;font-size:13px;font-weight:700;color:var(--green-link);margin-top:6px}
.forum-box{margin-top:16px;height:44px;background:var(--salmon);color:#fff;font-family:"Barlow",sans-serif;font-size:19px;line-height:20px;letter-spacing:1.2px;text-align:center;padding-top:2px}
.faculty{position:relative;margin-top:20px;height:138px;background:linear-gradient(135deg,#b8a38f,#d9c4b1 45%,#9a8a7d)}
.faculty-note{position:absolute;left:34px;top:36px;width:174px;background:rgba(255,255,255,.78);color:var(--salmon);font-size:14px;font-weight:700;letter-spacing:1.3px;line-height:16px;text-align:center;padding:2px}
.faculty-note em{color:#555;font-size:12px;letter-spacing:.3px}
.cancer-list{margin-top:27px}
.cancer-list a{display:block;height:22px;margin-bottom:2px;background:var(--taupe);color:#fff;font-size:15px;text-align:center;line-height:22px;width:243px}
</style>
</head>
<body>

<header>
  <a class="brand" href="#"><span class="brand-dot"></span><span class="brand-name">TIDEL</span></a>
  <div class="search">
    <div class="search-field">Site Search</div>
    <span class="search-btn">Search</span>
    <span class="search-clear">×</span>
  </div>
  <nav class="nav">
    <a class="nav-tab about" href="#">About TIDEL</a>
    <a class="nav-tab ask" href="#">Ask Us<br>Discussion Forums</a>
    <a class="nav-tab general" href="#">General<br>Cancer Info</a>
    <a class="nav-tab focused" href="#">Focused<br>Cancer Info</a>
    <a class="nav-tab profile" href="#">Profile</a>
    <a class="nav-tab donate" href="#">Donate
      <span class="donate-badge"><svg width="26" height="26" viewBox="0 0 26 26"><circle cx="13" cy="13" r="11" fill="#fff"/><path d="M13 7v12M7 13h12" stroke="#5cbf6a" stroke-width="3"/></svg></span>
    </a>
  </nav>
</header>

<section class="lead">
  <div role="img" aria-label="Photo of a smiling young cancer patient in a pink jacket" style="position:absolute;inset:0"></div>
  <h1 class="lead-title">Give to TIDEL.</h1>
  <p class="lead-sub">Cancer patients find answers here.<br>Your donation makes that possible.</p>
  <a class="lead-cta" href="#">DONATE NOW</a>
</section>
<div class="lead-underline"></div>

<a class="edit" href="#">Edit</a>

<main class="news">
  <div class="news-head">
    <h2 class="news-title">Recent TIDEL News &amp; Posts</h2>
    <span class="share"><i></i><i></i><i></i><i></i>Share/Email/More</span>
  </div>

  <article class="post">
    <h3 class="post-title">Cancer Care In Crisis? The Halvern Health Academy's Report: Delivering High-Quality Cancer Care: Charting a New Course For a System in Crisis; Part I: The Current Landscape</h3>
    <p class="post-meta">by <b>Dr. Harlan</b> on Nov 10, 2013 in <span class="cat">TIDEL :: Cancer Basics</span></p>
    <p class="post-text">&nbsp;A few months ago, the Halvern Health Academy released the prepublication proofs of a massive report on the state of oncology care, saying that it was in crisis in the United States. I learned about it from an email that focused on the crisis part of the title. I was bo... <em>(Read More)</em></p>
  </article>

  <article class="post">
    <h3 class="post-title">Is there a place for live educational meetings in our new online world? Would you want to come?</h3>
    <p class="post-meta">by <b>Dr Marsh</b> on Nov 8, 2013 in <span class="cat">TIDEL :: Lung Cancer</span></p>
    <p class="post-text">Back in 2009, TIDEL did a live educational meeting in Seattle, geared toward patients and caregivers, that coincided with a lung cancer conference offered to physicians. It included brief (~15 minute) talks by about 10 different specialists, ranging in topics from initi... <em>(Read More)</em></p>
  </article>

  <article class="post">
    <h3 class="post-title">Live Chat Thursday: The Tissue is the Issue, Key Challenges in Biopsies and Tissue Collection</h3>
    <p class="post-meta">by <b>Dr Marsh</b> on Nov 5, 2013 in <span class="cat">TIDEL :: Lung Cancer</span></p>
    <p class="post-text">This Thursday, November 7th at 8 PM Eastern, 5 PM Pacific, we'll gather in the chatverse for another one hour #LCTD (lung cancer community) chat. This time, the topic will be on biopsies and tissue collection.&nbsp; Now that we've entered a new era where more an... <em>(Read More)</em></p>
  </article>
</main>

<aside class="side">
  <div class="social">
    <span style="background:#4d6fa8"></span><span style="background:#7cc7e6"></span><span style="background:#c8302a"></span><span style="background:#e8893a"></span>
  </div>
  <a class="ask-box" href="#"><span class="qa">Q:</span><span class="qa">A:</span><span class="label">Ask Us</span></a>

  <h3>Welcome To TIDEL!</h3>
  <nav class="side-links">
    <a href="#" style="margin-top:10px">How To Use TIDEL</a>
    <a href="#">General Cancer FAQs</a>
    <a href="#" style="margin-top:12px">Recent TIDEL Site Post Comments</a>
  </nav>

  <div class="forum-box">TIDEL<br>Discussion Forums</div>
  <nav class="side-links">
    <a href="#" style="margin-top:12px">TIDEL Discussion Forum Guidelines</a>
    <a href="#" style="margin-top:12px">Recent TIDEL Forum Activity</a>
    <a href="#" style="margin-top:12px">Original TIDEL Archived Forums</a>
  </nav>

  <a class="faculty" href="#" style="display:block">
    <span role="img" aria-label="Grid of faculty member portrait photos" style="position:absolute;inset:0"></span>
    <span class="faculty-note">TIDEL is eager to bring in more great faculty members...<br><em>Interested? Click Here!</em></span>
  </a>

  <nav class="cancer-list">
    <a href="#">Lung/Thoracic Cancer Info</a>
    <a href="#">Breast Cancer Info</a>
    <a href="#">Pancreatic Cancer Info</a>
    <a href="#">Kidney Cancer Info</a>
    <a href="#">Bladder Cancer Info</a>
    <a href="#">Head/Neck Cancer Info</a>
  </nav>
</aside>

</body>
</html>
```